"Velmora Kestrel Bridgeworks": unique end to end Chinese marketing and ecommerce solutions*

I would like to create a company website for my trademark: "Velmora Kestrel Bridgeworks". We are based in Iceland. We are the only company in the market offering end-to-end Chinese digital marketing and eCommerce solutions. We help companies grow their brands and sales towards Chinese - whether tourism, export of products or services.
I include the logo that we have come up with in terms of colours and fonts.
The font is Trajan - I would like to use normal letters (capital and lowercase) for text.
Front page: Picture with colour filter. Logo in white. Text line underneath.
I am inspired by this website:
https://www.pelorumgrove.example/
I like these short videos for landing page:
https://www.framelodex.example/video/clip-30417852-ridge-scenic-vista-mountains
https://www.framelodex.example/video/clip-2093847155-4k-aerial-video-ridge-path-vista
https://www.framelodex.example/video/clip-3058172649-ridge-path-vista
Icelandic businesses looking for business opportunities in China or to attract Chinese tourists.
Digital Marketing

```html
<!DOCTYPE html>
<html lang="en">
<head>
<meta charset="utf-8">
<title>Velmora Kestrel Bridgeworks</title>
<link rel="stylesheet" href="https://fonts.googleapis.com/css2?family=Cinzel:wght@400;600;700&family=Open+Sans:ital,wght@0,400;0,600;1,600&family=Kaushan+Script&display=swap">
<style>
:root{
  --blue:#0d3f96;
  --gold:#a87a36;
  --ink:#222;
  --body:#555;
  --line:#cfcfcf;
  --footer:#1c1c1c;
  --grey:#ececec;
}
*{box-sizing:border-box;margin:0;padding:0}
html,body{width:1200px;height:3778px;overflow:hidden}
body{position:relative;background:#fff;font-family:"Open Sans",sans-serif;color:var(--body)}
.abs{position:absolute}

/* header */
.site-header{left:0;top:0;width:1200px;height:75px;background:#fff}
.brand{left:110px;top:22px;display:flex;align-items:center;gap:10px}
.brand-dot{width:28px;height:28px;border-radius:50%;background:var(--gold)}
.brand-name{font-family:"Cinzel",serif;font-weight:600;font-size:17px;color:var(--blue);letter-spacing:.5px}
.main-nav{left:571px;top:30px;display:flex;gap:34px;font-family:"Cinzel",serif;font-size:13px;color:var(--ink);letter-spacing:.5px}
.main-nav .active{color:var(--blue)}

/* hero */
.hero{left:0;top:75px;width:1200px;height:538px;background:linear-gradient(160deg,#3b3128 0%,#5a4a3c 35%,#2f2822 70%,#4c4036 100%)}
.hero-shade{left:0;top:75px;width:1200px;height:538px;background:rgba(20,15,10,.35)}
.hero-title{left:0;top:162px;width:1200px;text-align:center;font-family:"Cinzel",serif;font-size:64px;font-weight:400;color:#fff;letter-spacing:2px;line-height:1}
.hero-sub{left:0;top:243px;width:1200px;text-align:center;font-family:"Cinzel",serif;font-size:24px;color:#fff;letter-spacing:2px}
.play{left:571px;top:286px;width:58px;height:58px}
.btn-gold{background:var(--gold);color:#fff;font-family:"Cinzel",serif;border-radius:24px;text-align:center;letter-spacing:1px}
.hero-btn{left:505px;top:377px;width:192px;height:41px;line-height:41px;font-size:17px}
.chev{left:588px;top:490px}

/* services */
.card{top:553px;width:319px;height:286px;background:#fff;border:1px solid #ddd;box-shadow:0 2px 8px rgba(0,0,0,.12);padding:0 31px}
.card h3{font-family:"Cinzel",serif;font-weight:600;font-size:20px;color:var(--ink);letter-spacing:1px;line-height:24px}
.card p{font-size:13px;line-height:25.5px}
.card.featured{background:var(--blue);border-color:var(--blue)}
.card.featured h3,.card.featured p{color:#fff}

/* about */
.about-img{left:141px;top:896px;width:441px;height:298px;background:linear-gradient(135deg,#0c1a3f,#1d3a7a 45%,#7b1d4a 75%,#1a1230)}
.about-title{left:645px;top:957px;font-family:"Cinzel",serif;font-size:46px;font-weight:600;color:var(--ink)}
.about-text{left:650px;top:1022px;width:400px;font-size:13px;line-height:25.5px}

/* why */
.sec-title{left:0;width:1200px;text-align:center;font-family:"Cinzel",serif;font-size:46px;color:var(--ink);font-weight:600}
.why-lead{left:0;top:1360px;width:1200px;text-align:center;font-size:22px;line-height:31px;color:#444}
.why-img{top:1470px;width:309px;height:202px}
.why-num{top:1702px;width:48px;height:48px;border-radius:50%;background:var(--gold);color:#fff;font-style:italic;font-weight:600;font-size:22px;text-align:center;line-height:48px}
.why-name{top:1702px;font-family:"Cinzel",serif;font-size:32px;color:var(--ink)}
.why-text{top:1746px;width:232px;font-size:12.5px;line-height:20.5px}

/* important */
.important-band{left:0;top:1840px;width:1200px;height:380px;background:radial-gradient(ellipse at 55% 45%,#d7d7d7 0%,#ececec 35%,#f7f7f7 60%,#fff 80%)}
.imp-icon{left:200px;top:1951px;width:64px;height:64px;border-radius:50%;background:#e0222b;color:#fff;font-weight:700;font-size:40px;text-align:center;line-height:64px}
.imp-word{left:270px;top:1955px;font-family:"Kaushan Script",cursive;font-size:34px;color:#333}
.imp-rule{left:402px;top:1950px;width:1px;height:78px;background:#bbb}
.imp-text{left:420px;top:1963px;width:584px;text-align:center;font-size:15px;line-height:21px;color:#555}

/* testimonials */
.tcard{text-align:center;font-size:14px;line-height:20.5px;color:#333}
.tcard.side{top:2255px;height:198px;background:var(--grey);padding:25px 12px 0}
.tcard.main{left:424px;top:2222px;width:355px;height:273px;background:#fff;border-radius:10px;box-shadow:0 8px 20px rgba(0,0,0,.12);padding:30px 44px 0;font-size:15px;line-height:21px;z-index:2}
.stars{color:#f29b12;letter-spacing:13px;font-size:14px;margin-top:6px}
.tname{font-weight:600;color:#222;margin-top:2px}

/* faq */
.faq-band{left:0;top:2580px;width:1200px;height:260px}
.faq-title{left:0;top:2660px;width:1200px;text-align:center;font-family:"Kaushan Script",cursive;font-size:52px;color:#fff}

/* contact */
.field{left:147px;width:440px;border:1px solid var(--line);padding:0 22px;font-size:15px;color:#333}
.submit{left:147px;top:3336px;width:164px;height:44px;line-height:44px;font-size:19px;border-radius:22px}
.info-icon{left:688px}
.info-text{left:758px;font-size:13.5px;line-height:18.5px;color:#222}
.map{left:684px;top:3194px;width:382px;height:212px;border:2px solid var(--gold);background:linear-gradient(135deg,#eef0e6,#dfe6d5 50%,#e9ece2)}

/* footer */
.site-footer{left:0;top:3477px;width:1200px;height:301px;background:var(--footer)}
.foot-brand{left:0;top:3525px;width:1200px;display:flex;justify-content:center;align-items:center;gap:14px}
.foot-brand .brand-name{color:var(--gold);font-size:24px;font-weight:400}
.foot-nav{left:0;top:3607px;width:1200px;display:flex;justify-content:center;gap:32px;font-size:14px;color:#fff}
.foot-social{left:0;top:3663px;width:1200px;display:flex;justify-content:center;gap:24px;font-size:17px;color:#fff}
.foot-social span{display:flex;align-items:center;gap:10px}
.foot-social i{width:10px;height:10px;border-radius:50%;background:#fff;display:inline-block}
.copy{left:0;top:3714px;width:1200px;text-align:center;font-size:11px;color:var(--gold)}
</style>
</head>
<body>

<header class="abs site-header">
  <div class="abs brand"><span class="brand-dot"></span><span class="brand-name">Velmora Kestrel Bridgeworks</span></div>
  <nav class="abs main-nav"><span class="active">Home</span><span>About Us</span><span>Services</span><span>Testimonials</span><span>Contact Us</span></nav>
</header>

<section>
  <div class="abs hero" role="img" aria-label="Aerial footage of a stone path winding over mountain ridges"></div>
  <div class="abs hero-shade"></div>
  <h1 class="abs hero-title">Velmora Kestrel</h1>
  <div class="abs hero-sub">Bridgeworks</div>
  <svg class="abs play" viewBox="0 0 58 58"><circle cx="29" cy="29" r="29" fill="#1a1a1a"/><path d="M23 19 L39 29 L23 39Z" fill="#fff"/></svg>
  <div class="abs btn-gold hero-btn">Learn More</div>
  <svg class="abs chev" width="24" height="16" viewBox="0 0 24 16"><path d="M4 4 L12 12 L20 4" stroke="#fff" stroke-width="2.5" fill="none"/></svg>
</section>

<section>
  <article class="abs card" style="left:111px;padding-top:34px">
    <h3>Ecommerce</h3>
    <p style="margin-top:22px">Lorem ipsum dolor sit amet, consectetur adipiscing elit, sed do eiusmod tempor incididunt ut labore et dolore magna aliqua. Ut enim ad minim veniam, quis nostrud exercitation ullamco laboris nisi ut aliquip ex ea commodo consequat.</p>
  </article>
  <article class="abs card featured" style="left:444px;padding-top:20px">
    <h3>Chinese -<br>whether Tourism</h3>
    <p style="margin-top:12px">Lorem ipsum dolor sit amet, consectetur adipiscing elit, sed do eiusmod tempor incididunt ut labore et dolore magna aliqua. Ut enim ad minim veniam, quis nostrud exercitation ullamco laboris nisi ut aliquip ex ea commodo consequat.</p>
  </article>
  <article class="abs card" style="left:776px;padding-top:20px">
    <h3>Export of Products</h3>
    <p style="margin-top:22px">Lorem ipsum dolor sit amet, consectetur adipiscing elit, sed do eiusmod tempor incididunt ut labore et dolore magna aliqua. Ut enim ad minim veniam, quis nostrud exercitation ullamco laboris nisi ut aliquip ex ea commodo consequat.</p>
  </article>
</section>

<section>
  <div class="abs about-img" role="img" aria-label="Person working with a glowing digital network display"></div>
  <h2 class="abs about-title">About Us</h2>
  <p class="abs about-text">Lorem ipsum dolor sit amet, consectetur adipiscing elit, sed do eiusmod tempor incididunt ut labore et dolore magna aliqua. Ut enim ad minim veniam, quis nostrud exercitation ullamco laboris nisi ut aliquip ex ea commodo consequat.</p>
</section>

<section>
  <h2 class="abs sec-title" style="top:1278px">Why Choose Us</h2>
  <p class="abs why-lead">Sed ut perspiciatis unde omnis iste natus error sit voluptatem accusantium<br>doloremque laudantium, totam rem aperiam, eaque ipsa</p>

  <div class="abs why-img" style="left:111px;background:linear-gradient(135deg,#dfe6e2,#b9c7c2 50%,#eef0ee)" role="img" aria-label="Businessman working on a laptop in a bright office"></div>
  <div class="abs why-img" style="left:446px;background:linear-gradient(160deg,#0e2d6e,#2f6bc4 45%,#0a1633 80%,#6a3a1e)" role="img" aria-label="Businessman facing a city skyline at night with digital overlays"></div>
  <div class="abs why-img" style="left:782px;background:linear-gradient(135deg,#e9e9e9,#cfcfcf 50%,#3a3a3a)" role="img" aria-label="Team meeting around a conference table"></div>

  <div class="abs why-num" style="left:114px">01</div>
  <div class="abs why-name" style="left:172px">Lorium</div>
  <p class="abs why-text" style="left:170px">Sed ut perspiciatis unde omnis iste natus error sit voluptatem accusantium doloremque laudantium, totam rem aperiam, eaque ipsa</p>

  <div class="abs why-num" style="left:465px">02</div>
  <div class="abs why-name" style="left:527px;top:1698px">Ipsum</div>
  <p class="abs why-text" style="left:524px">Sed ut perspiciatis unde omnis iste natus error sit voluptatem accusantium doloremque laudantium, totam rem aperiam, eaque ipsa</p>

  <div class="abs why-num" style="left:799px">03</div>
  <div class="abs why-name" style="left:860px">Dolor</div>
  <p class="abs why-text" style="left:859px">Sed ut perspiciatis unde omnis iste natus error sit voluptatem accusantium doloremque laudantium, totam rem aperiam, eaque ipsa</p>
</section>

<section>
  <div class="abs important-band" role="img" aria-label="Soft misty mountain range backdrop"></div>
  <div class="abs imp-icon">!</div>
  <div class="abs imp-word">Important</div>
  <div class="abs imp-rule"></div>
  <p class="abs imp-text">Sed ut perspiciatis unde omnis iste natus error sit voluptatem accusantium doloremque laudantium, totam rem aperiam, eaque ipsa</p>
</section>

<section>
  <h2 class="abs sec-title" style="top:2128px">Testimonials</h2>
  <div class="abs tcard side" style="left:144px;width:281px;padding-right:0">
    <p>Lorem ipsum dolor sit amet, consectetur adipiscing elit, sed do eiusmod tempor incididunt ut labore et dolore magna aliqua.exercitation ullamco...</p>
    <div class="stars">★★★★★</div>
    <div class="tname">- David</div>
  </div>
  <div class="abs tcard main">
    <p>Lorem ipsum dolor sit amet, consectetur adipiscing elit, sed do eiusmod tempor incididunt ut labore et dolore magna aliqua. Ut enim ad minim veniam, quis nostrud exercitation ullamco...</p>
    <div class="stars" style="margin-top:26px">★★★★★</div>
    <div class="tname" style="margin-top:10px">- Jhon Smith</div>
  </div>
  <div class="abs tcard side" style="left:778px;width:278px;padding-left:0">
    <p>Lorem ipsum dolor sit amet, consectetur adipiscing elit, sed do eiusmod tempor incididunt ut labore et dolore magna aliqua.exercitation ullamco...</p>
    <div class="stars">★★★★★</div>
    <div class="tname">-Riya</div>
  </div>
</section>

<section>
  <svg class="abs faq-band" viewBox="0 0 1200 260" preserveAspectRatio="none"><path d="M0 40 Q150 20 300 34 T600 28 T900 22 T1200 8 L1200 205 Q1050 215 900 222 T600 232 T300 236 T0 252 Z" fill="#0d3f96"/></svg>
  <h2 class="abs faq-title">Frequently Asked Questions</h2>
</section>

<section>
  <h2 class="abs sec-title" style="top:2884px;font-weight:400">Contact Us</h2>
  <div class="abs field" style="top:3009px;height:50px;line-height:48px">Name</div>
  <div class="abs field" style="top:3081px;height:50px;line-height:48px">Email</div>
  <div class="abs field" style="top:3151px;height:50px;line-height:48px">Phone</div>
  <div class="abs field" style="top:3223px;height:91px;padding-top:14px">Message</div>
  <div class="abs btn-gold submit">Submit</div>

  <svg class="abs info-icon" style="top:3018px" width="16" height="18" viewBox="0 0 16 18"><path d="M8 1a5.5 5.5 0 0 0-5.5 5.5C2.5 11 8 17 8 17s5.5-6 5.5-10.5A5.5 5.5 0 0 0 8 1z" fill="#222"/><circle cx="8" cy="6.5" r="2" fill="#fff"/></svg>
  <p class="abs info-text" style="top:3017px">#48 Fjordvale Street,<br>Northmere,<br>Iceland.</p>
  <svg class="abs info-icon" style="top:3093px" width="16" height="16" viewBox="0 0 16 16"><path d="M3 1l3 3-1.5 2c1 2 3 4 5 5l2-1.5 3 3-2 2C6 14 2 10 1 3z" fill="#222"/></svg>
  <p class="abs info-text" style="top:3092px">1-800 555 0142</p>
  <svg class="abs info-icon" style="top:3133px" width="16" height="12" viewBox="0 0 16 12"><rect width="16" height="12" fill="#222"/><path d="M0 1 L8 7 L16 1" stroke="#fff" stroke-width="1.3" fill="none"/></svg>
  <p class="abs info-text" style="top:3130px">info@velmorakestrel.example</p>
  <div class="abs map" role="img" aria-label="Location map"></div>
</section>

<footer class="abs site-footer"></footer>
<div class="abs foot-brand"><span class="brand-dot" style="width:34px;height:34px"></span><span class="brand-name">Velmora Kestrel Bridgeworks</span></div>
<nav class="abs foot-nav"><span>Home</span><span>About Us</span><span>Services</span><span>Why Choose Us</span><span>Testimonials</span><span>Contact Us</span></nav>
<div class="abs foot-social"><span><i></i>Linkora</span><span><i></i>Chirpvale</span><span><i></i>Snapmere</span></div>
<p class="abs copy">© 2020 | www.velmorakestrel.example</p>

</body>
</html>
```